Log In Screen Design

We have an existing website (www.velmarix4.com) and have recently developed software which requires a login screen using a similar theme from the velmarix4 website. The login screen should have a username and password. The software title is Outcome Tiered Scheduling (OTS). The VELMARIX4 log should appear on the login screen and the page should look professional.
Target Market(s)
Project Management Professionals
Industry/Entity Type
Software
Requirements
Must have
- Username and password blocks
Company Logo
Company Name - VELMARIX4 Management Ltd
Software Name - Outcome Tiered Scheduling (OTS)
Similar theme (colors) to the logo and existing website

```html
<!DOCTYPE html>
<html lang="en">
<head>
<meta charset="utf-8">
<title>OTS Login</title>
<link href="https://fonts.googleapis.com/css2?family=Open+Sans:wght@400;600;700&family=Michroma&display=swap" rel="stylesheet">
<style>
  :root {
    --bg-deep: #0f2b4d;
    --bg-mid: #3d6591;
    --bg-light: #b9d6ef;
    --card-top: #f7f7f7;
    --card-bottom: #bdbdbd;
    --rule: #8a8a8a;
    --ink: #1c1c1c;
    --label: #555555;
    --brand-grey: #6a6a6a;
    --brand-blue: #2a6fbf;
    --button: #6b6b6b;
    --tab: #6e6e6e;
    --field: #ffffff;
  }
  html, body { margin: 0; padding: 0; overflow: hidden; }
  body {
    width: 1200px; height: 1000px; position: relative;
    background:
      radial-gradient(ellipse 260px 600px at 1020px 250px, rgba(205,228,247,0.85), rgba(205,228,247,0) 70%),
      radial-gradient(ellipse 300px 500px at 880px 650px, rgba(140,185,225,0.5), rgba(140,185,225,0) 70%),
      radial-gradient(ellipse 700px 600px at 600px 250px, rgba(120,160,200,0.7), rgba(120,160,200,0) 70%),
      linear-gradient(160deg, #1a4474 0%, var(--bg-mid) 45%, #2a5486 70%, var(--bg-deep) 100%);
    font-family: "Open Sans", sans-serif;
  }
  .login-card {
    position: absolute; left: 449px; top: 311px; width: 311px; height: 381px;
    border-radius: 9px; overflow: hidden;
    background: linear-gradient(180deg, var(--card-top) 0%, #e6e6e6 30%, var(--card-bottom) 100%);
    box-shadow: 0 0 0 1px rgba(255,255,255,0.5);
  }
  .brand {
    height: 84px; border-bottom: 1px solid var(--rule);
    display: flex; align-items: center; justify-content: center; gap: 10px;
  }
  .brand-mark { width: 44px; height: 44px; border-radius: 50%; background: var(--brand-blue); }
  .brand-name {
    font-family: "Open Sans", sans-serif; font-weight: 400; font-size: 22px;
    letter-spacing: 1px; color: var(--brand-grey);
  }
  .app-title {
    text-align: center; margin: 26px 0 0; font-size: 37px; font-weight: 700;
    letter-spacing: 8px; color: var(--ink); line-height: 40px;
  }
  .app-subtitle {
    text-align: center; margin: 4px 0 0; font-size: 19px; color: var(--ink);
  }
  .login-form { position: absolute; left: 57px; top: 204px; width: 196px; }
  .field-label { display: block; font-size: 11px; color: var(--label); line-height: 14px; }
  .field-input {
    display: block; width: 196px; height: 21px; background: var(--field);
    border: none; margin: 0 0 8px; padding: 0; box-sizing: border-box;
  }
  .form-footer { position: relative; height: 20px; }
  .remember { position: absolute; left: 0; top: 0; font-size: 7px; color: var(--label); display: flex; align-items: center; gap: 2px; }
  .remember-dot { width: 7px; height: 7px; border-radius: 50%; background: #fff; box-shadow: inset 0 0 0 2px #fff, inset 0 0 0 4px #333; }
  .login-button {
    position: absolute; left: 130px; top: 0; width: 58px; height: 17px;
    background: var(--button); color: #fff; border: none; font-family: inherit;
    font-size: 10px; padding: 0;
  }
  .footer-tab { position: absolute; left: 60px; bottom: 0; width: 178px; height: 29px; }
  .footer-tab span {
    position: absolute; inset: 0; display: flex; align-items: center; justify-content: center;
    color: #fff; font-size: 9px;
  }
</style>
</head>
<body>
  <main class="login-card">
    <header class="brand">
      <span class="brand-mark"></span>
      <span class="brand-name">VELMARIX4</span>
    </header>
    <h1 class="app-title">OTS</h1>
    <p class="app-subtitle">Outcome Tiered Scheduling</p>
    <form class="login-form">
      <label class="field-label" for="username">User Name</label>
      <input class="field-input" id="username" type="text">
      <label class="field-label" for="password">Password</label>
      <input class="field-input" id="password" type="password">
      <div class="form-footer">
        <span class="remember"><span class="remember-dot"></span>Remember Me</span>
        <button class="login-button" type="button">Login</button>
      </div>
    </form>
    <div class="footer-tab">
      <svg width="178" height="29" viewBox="0 0 178 29"><polygon points="10,0 166,0 178,29 0,29" fill="var(--tab)"/></svg>
      <span>VELMARIX4 Management Ltd</span>
    </div>
  </main>
</body>
</html>
```